Bolstering Marveno Inc needs a business card design

Looking for a unique, classy and sharp business card design.

Contact Information for Business Card

Bolstering Marveno Inc.
Lidia Osorno Bermudez BScOT(c)
Occupational Therapist
(780) 555-0142
bolsteringmarveno@mailvora.com

```html
<!DOCTYPE html>
<html lang="en">
<head>
<meta charset="utf-8">
<title>Bolstering Marveno Inc. — Business Card</title>
<link href="https://fonts.googleapis.com/css2?family=Raleway:wght@400;700&display=swap" rel="stylesheet">
<style>
  :root {
    --purple-deep: #8a2390;
    --purple-mid: #a83eae;
    --purple-light: #c46ac8;
    --paper: #ffffff;
    --paper-shade: #ececec;
    --backdrop: #e9e6ea;
    --brand-green: #8cc63f;
  }
  * { box-sizing: border-box; margin: 0; padding: 0; }
  html, body {
    width: 1200px; height: 1022px; overflow: hidden;
    background: var(--backdrop);
    font-family: "Raleway", sans-serif;
  }
  .sheet {
    width: 1200px; height: 1022px;
    display: flex; flex-direction: column; align-items: center; justify-content: space-evenly;
  }
  .card {
    position: relative; width: 800px; height: 457px; overflow: hidden;
    border-radius: 4px;
    box-shadow: 0 8px 24px rgba(60, 30, 70, 0.18);
  }
  .card-front { background: var(--paper); }
  .card-back { background: linear-gradient(135deg, var(--purple-light), var(--purple-mid) 45%, var(--purple-deep)); }
  .swoosh { position: absolute; inset: 0; width: 100%; height: 100%; }
  .contact {
    position: absolute; color: var(--paper);
    width: 420px;
  }
  .card-front .contact { left: 330px; top: 48px; }
  .card-back .contact { left: 290px; top: 130px; }
  .contact-name { font-weight: 700; font-size: 25px; letter-spacing: 0.2px; }
  .contact-name .credential { font-weight: 400; }
  .contact-role { font-size: 21px; margin-top: 4px; }
  .contact-line {
    display: flex; justify-content: space-between; align-items: center;
    font-size: 20px; margin-top: 14px;
  }
  .contact-line:first-of-type { margin-top: 36px; }
  .contact-line svg { width: 16px; height: 16px; flex: none; }
  .brand {
    position: absolute; left: 70px; top: 345px;
    display: flex; align-items: center; gap: 14px;
    color: var(--purple-deep); font-weight: 700; font-size: 40px;
  }
  .brand-dot { width: 26px; height: 26px; border-radius: 50%; background: var(--brand-green); }
</style>
</head>
<body>
<main class="sheet">
  <section class="card card-front">
    <svg class="swoosh" viewBox="0 0 800 457" preserveAspectRatio="none" aria-hidden="true">
      <defs>
        <linearGradient id="frontPurple" x1="0" y1="0" x2="1" y2="1">
          <stop offset="0" stop-color="#c46ac8"/>
          <stop offset="0.5" stop-color="#a83eae"/>
          <stop offset="1" stop-color="#8a2390"/>
        </linearGradient>
      </defs>
      <path d="M0 0 H800 V175 C560 215 300 265 0 330 Z" fill="url(#frontPurple)"/>
      <path d="M800 182 C620 210 470 235 360 258 C500 240 660 222 800 214 Z" fill="#ffffff"/>
      <path d="M800 214 C680 220 560 232 470 244 C580 238 700 236 800 238 Z" fill="#b552ba" opacity="0.8"/>
    </svg>
    <div class="contact">
      <p class="contact-name">Lidia Osorno Bermudez <span class="credential">BScOT(c)</span></p>
      <p class="contact-role">Occupational Therapist</p>
      <p class="contact-line"><span>(780) 555-0142</span>
        <svg viewBox="0 0 16 16"><path d="M4 1 L6.5 4 L5 6 C6 8.5 7.5 10 10 11 L12 9.5 L15 12 L13 15 C7 14.5 1.5 9 1 3 Z" fill="#fff"/></svg>
      </p>
      <p class="contact-line"><span>bolsteringmarveno@mailvora.com</span>
        <svg viewBox="0 0 16 16"><rect x="1" y="3" width="14" height="10" fill="#fff"/><path d="M1 3 L8 9 L15 3" fill="none" stroke="#a83eae" stroke-width="1.4"/></svg>
      </p>
    </div>
    <div class="brand"><span class="brand-dot"></span><span>Bolstering Marveno Inc.</span></div>
  </section>

  <section class="card card-back">
    <div class="contact">
      <p class="contact-name">Lidia Osorno Bermudez <span class="credential">BScOT(c)</span></p>
      <p class="contact-role">Occupational Therapist</p>
      <p class="contact-line"><span>(780) 555-0142</span>
        <svg viewBox="0 0 16 16"><path d="M4 1 L6.5 4 L5 6 C6 8.5 7.5 10 10 11 L12 9.5 L15 12 L13 15 C7 14.5 1.5 9 1 3 Z" fill="#fff"/></svg>
      </p>
      <p class="contact-line"><span>bolsteringmarveno@mailvora.com</span>
        <svg viewBox="0 0 16 16"><rect x="1" y="3" width="14" height="10" fill="#fff"/><path d="M1 3 L8 9 L15 3" fill="none" stroke="#a83eae" stroke-width="1.4"/></svg>
      </p>
    </div>
  </section>
</main>
</body>
</html>
```